Company business card

We need a new business card design. We are IT company which is specialized for outsourcing of operations hardware and software (specially Velbrandt, we are a partner), developing custom applications and web applications, BPM solutions, auditing hw and sw. actually design was attached. But we need completely NEW.

Industry/Entity Type

Business

```html
<!DOCTYPE html>
<html lang="en">
<head>
<meta charset="utf-8">
<title>KORVEX business card</title>
<link rel="stylesheet" href="https://fonts.googleapis.com/css2?family=Open+Sans:wght@400;600;700&display=swap">
<style>
  :root {
    --page-bg: #2e2927;
    --card-dark: #151515;
    --card-dark-edge: #262626;
    --band-grey: #7a7a7a;
    --card-grey: #7b7b7b;
    --ink-light: #ffffff;
    --ink-soft: #e6e6e6;
    --rule: #9a9a9a;
  }
  html, body {
    margin: 0;
    padding: 0;
    width: 1200px;
    height: 844px;
    overflow: hidden;
    background: var(--page-bg);
    font-family: "Open Sans", Arial, sans-serif;
  }
  .stage {
    position: relative;
    width: 1200px;
    height: 844px;
  }
  .card {
    position: absolute;
    top: 260px;
    width: 500px;
    height: 324px;
    box-shadow: 0 12px 30px rgba(0,0,0,0.45);
    overflow: hidden;
  }
  .card-back {
    left: 70px;
    background: var(--band-grey);
  }
  .card-back .panel {
    position: absolute;
    left: 0; right: 0;
    top: 18px; bottom: 18px;
    background: linear-gradient(90deg, var(--card-dark) 0%, var(--card-dark) 70%, var(--card-dark-edge) 100%);
    display: flex;
    flex-direction: column;
    align-items: center;
    justify-content: center;
    color: var(--ink-light);
    text-align: center;
  }
  .person-name {
    font-weight: 600;
    font-size: 15px;
    letter-spacing: 0.3px;
    padding: 0 4px 3px;
    border-bottom: 1px solid var(--rule);
    margin: 0;
  }
  .person-role {
    font-size: 11px;
    color: var(--ink-soft);
    margin: 4px 0 26px;
  }
  .contact-list {
    list-style: none;
    margin: 0 0 22px;
    padding: 0;
    font-size: 12.5px;
    line-height: 1.35;
  }
  .company-name {
    font-weight: 700;
    font-size: 13.5px;
    margin: 0 0 6px;
  }
  .company-address {
    font-size: 14px;
    color: var(--ink-soft);
    margin: 0;
  }
  .card-front {
    left: 630px;
    background: var(--card-grey);
    display: flex;
    align-items: center;
    justify-content: center;
  }
  .brand {
    display: flex;
    align-items: center;
    gap: 12px;
    color: var(--ink-light);
    margin-bottom: 40px;
  }
  .brand-square {
    width: 46px;
    height: 46px;
  }
  .brand-name {
    font-weight: 700;
    font-size: 34px;
    letter-spacing: 1px;
    line-height: 1;
  }
</style>
</head>
<body>
  <main class="stage">
    <section class="card card-back" aria-label="Card back with contact details">
      <div class="panel">
        <h1 class="person-name">MAREK VANDA</h1>
        <p class="person-role">CEO</p>
        <ul class="contact-list">
          <li>+421 (0) 900 555 214</li>
          <li>marek.vanda@korvex.sk</li>
          <li>www.korvex.sk</li>
        </ul>
        <p class="company-name">KORVEX s.r.o</p>
        <p class="company-address">Lipova 12 811 02 Bratislava</p>
      </div>
    </section>

    <section class="card card-front" aria-label="Card front with company name">
      <div class="brand">
        <svg class="brand-square" viewBox="0 0 46 46" aria-hidden="true">
          <rect width="46" height="46" fill="#ffffff"/>
        </svg>
        <span class="brand-name">KORVEX</span>
      </div>
    </section>
  </main>
</body>
</html>
```